Brisk Heron Crypto Token Website

Website for a new crypto currency backed up by a hedge fund, 4-5 pages. Needs to have a modern finance, investment, wall street, crypto, tech feel. Looking for the "cool webpage" response. Looking for big pictures and the feel of an Advertisement. Not a lot of white space. Pages will not be content heavy: 1) Brisk Heron/Investment Case 2) Statistics 3) How to Buy 4) Media/Community
Please create a coin mockup in gold
please work on logo
bring crypto images into the page

Target Market(s)

Investors, News outlets

Industry/Entity Type

Business, Finance, Crypto

Coding

Coded - Design and coding required

Number of Pages Required

5+ page

Font styles to use
Serif

Requirements
Must have
• must catch attention right away, must have serious/ business /modern /tech / cool feel
Nice to have
• Look professional, look like ad (big pictures), animation?
Should not have
• too many colors

```html
<!DOCTYPE html>
<html lang="en">
<head>
<meta charset="utf-8">
<title>Brisk Heron LLC — Wall Street meets Crypto</title>
<link rel="stylesheet" href="https://fonts.googleapis.com/css2?family=IBM+Plex+Sans:wght@500;600;700&family=Heebo:wght@400;500&family=Poppins:ital,wght@0,400;0,500;0,600;1,400&display=swap">
<style>
:root{
  --navy-deep:#040b1c;
  --navy:#071431;
  --navy-mid:#0b1d45;
  --hero-blue:#0f2a8c;
  --teal:#16879a;
  --link:#2f74c0;
  --white:#ffffff;
  --muted:#d2d9e6;
  --footer:#0b1425;
  --card:#0f1a30;
}
*{margin:0;padding:0;box-sizing:border-box}
html,body{width:1200px;height:4075px;overflow:hidden;background:var(--navy-deep);color:var(--white)}
body{position:relative;font-family:"Heebo",Arial,sans-serif}
.abs{position:absolute}
.heading{font-family:"IBM Plex Sans",Arial,sans-serif;font-weight:600;letter-spacing:.5px;text-transform:uppercase}
.btn{position:absolute;display:flex;align-items:center;justify-content:center;background:var(--teal);border-radius:26px;font-family:"Poppins",Arial,sans-serif;font-weight:600;font-size:15px;letter-spacing:.5px;color:var(--white);text-transform:uppercase}

/* hero */
.hero{left:0;top:0;width:1200px;height:685px;background:radial-gradient(ellipse at 62% 40%,#1c47c9 0%,#123199 35%,#0b1f6a 70%,#081752 100%)}
.brand{left:100px;top:24px;width:240px;text-align:center}
.brand-mark{width:46px;height:46px;border-radius:50%;background:var(--teal);margin:0 auto 10px}
.brand-name{font-family:"IBM Plex Sans",Arial,sans-serif;font-weight:600;font-size:20px}
.brand-tag{font-family:"Heebo",Arial,sans-serif;font-size:14px;margin-top:2px}
.nav{top:36px;left:553px;font-family:"Heebo",Arial,sans-serif;font-weight:500;font-size:17px;letter-spacing:.4px}
.nav span{position:absolute;white-space:nowrap}
.globe{left:620px;top:130px;width:500px;height:480px;border-radius:50%;background:radial-gradient(circle at 50% 42%,#7fd0ff 0%,#2f86f0 22%,#1b4fd0 45%,rgba(18,49,153,0) 70%)}
.hero-title{left:111px;top:268px;font-size:41px;line-height:48px}
.hero-sub{left:111px;top:316px;font-family:"IBM Plex Sans",Arial,sans-serif;font-weight:500;font-size:30px;letter-spacing:.5px}
.hero-text{left:111px;top:356px;width:430px;font-size:14.5px;line-height:26px}
.dots{display:flex;gap:14px}
.dot{width:11px;height:11px;border-radius:50%;background:#8e9bbd}
.dot.on{background:var(--white)}

/* sections */
.band{left:0;width:1200px}
.invest{top:685px;height:670px;background:var(--navy-deep)}
.about{top:1355px;height:558px;background:linear-gradient(180deg,#0a1636 0%,#0d2150 50%,#081433 100%)}
.coin{top:1913px;height:680px;background:var(--navy-deep)}
.testi{top:2593px;height:498px;background:linear-gradient(180deg,#07112b 0%,#0c1f4a 55%,#07112b 100%)}
.blog{top:3091px;height:648px;background:var(--navy-deep)}
.footer{top:3739px;height:336px;background:var(--footer)}

.photo{position:absolute;border-radius:3px}
.sec-title{font-size:36px;line-height:42px}
.bullets{list-style:none;font-size:12.5px;line-height:23.5px;color:var(--white)}
.bullets li{position:relative;padding-left:16px;margin-bottom:9px}
.bullets li::before{content:"";position:absolute;left:0;top:7px;width:8px;height:8px;border:1.5px solid var(--white);border-radius:50%;box-shadow:inset 0 0 0 1.5px var(--navy-deep);background:var(--white)}
.body-text{font-size:13px;line-height:23.3px;color:var(--white)}

.quote{left:200px;top:2796px;width:800px;text-align:center;font-family:"Poppins",Arial,sans-serif;font-style:italic;font-size:14.5px;line-height:30.5px;color:var(--muted)}
.quote-badge{left:572px;top:2734px;width:56px;height:56px;border:2px solid var(--white);border-radius:50%;display:flex;align-items:center;justify-content:center;font-family:"Poppins",Arial,sans-serif;font-weight:600;font-size:40px;line-height:1;padding-top:14px}
.avatar{left:451px;top:2930px;width:53px;height:53px;border-radius:50%;background:linear-gradient(160deg,#c9b7a5,#6d5646)}
.author{left:520px;top:2930px;font-family:"Poppins",Arial,sans-serif}
.author b{display:block;font-weight:600;font-size:17px;line-height:24px}
.author span{font-size:14.5px;line-height:24px;color:var(--muted)}

.card{position:absolute;top:3241px;width:312px;height:408px;background:var(--card);border-radius:3px;overflow:hidden}
.card-img{height:214px}
.card-body{padding:20px 14px 0}
.card-title{font-family:"Poppins",Arial,sans-serif;font-weight:600;font-size:17.5px;line-height:27px}
.card-text{font-size:12.5px;line-height:24px;margin-top:14px;color:var(--muted)}
.card-more{display:block;margin-top:10px;font-family:"Poppins",Arial,sans-serif;font-weight:600;font-size:12.5px;color:var(--link);text-decoration:underline;text-transform:uppercase}

.f-col{position:absolute;top:3808px}
.f-col h4{font-family:"IBM Plex Sans",Arial,sans-serif;font-weight:600;font-size:19px;margin-bottom:11px}
.f-col p{font-size:15px;line-height:28px;color:var(--muted)}
.email{left:775px;top:3856px;width:313px;height:49px;background:var(--white);border-radius:25px;color:#333;font-family:"Poppins",Arial,sans-serif;font-size:14px;padding:13px 25px}
.rule{left:112px;top:4000px;width:976px;height:1px;background:#2a3650}
.copy{left:0;top:4025px;width:1200px;text-align:center;font-size:14.5px;color:var(--muted)}
</style>
</head>
<body>

<section class="abs hero">
  <div class="abs globe" role="img" aria-label="Glowing digital globe with a crypto coin emblem on a light ring"></div>
  <div class="abs brand">
    <div class="brand-mark"></div>
    <div class="brand-name">BRISK HERON LLC</div>
    <div class="brand-tag">“Wall Street meets Crypto”</div>
  </div>
  <nav class="abs nav">
    <span style="left:0">BRISK HERON</span>
    <span style="left:166px">STATISTICS</span>
    <span style="left:298px">HOW TO BUY</span>
    <span style="left:432px">COMMUNITY</span>
  </nav>
  <h1 class="abs heading hero-title">Brisk Heron LLC</h1>
  <div class="abs hero-sub">WALL STREET MEETS CRYPTO</div>
  <p class="abs hero-text">Lorem ipsum dolor sit amet, consectetur adipiscing elit, sed do eiusmod tempor incididunt ut labore et dolore magna aliqua. Quis ipsum suspendisse ultrices gravida.</p>
  <div class="btn" style="left:111px;top:452px;width:174px;height:48px">Get Started</div>
  <svg class="abs" style="left:68px;top:345px" width="22" height="44" viewBox="0 0 22 44"><polyline points="20,2 2,22 20,42" fill="none" stroke="#fff" stroke-width="2"/></svg>
  <svg class="abs" style="left:1110px;top:345px" width="22" height="44" viewBox="0 0 22 44"><polyline points="2,2 20,22 2,42" fill="none" stroke="#fff" stroke-width="2"/></svg>
  <div class="abs dots" style="left:558px;top:646px"><i class="dot"></i><i class="dot on"></i><i class="dot"></i><i class="dot"></i></div>
</section>

<section class="abs band invest"></section>
<div class="photo" style="left:128px;top:768px;width:466px;height:473px;background:radial-gradient(circle at 45% 65%,#e0b040 0%,#b07a1c 25%,#5a3a18 50%,#1d2436 80%)" role="img" aria-label="Gold crypto coin in front of a stock ticker board"></div>
<h2 class="abs heading sec-title" style="left:645px;top:786px">Investment Case</h2>
<ul class="abs bullets" style="left:645px;top:843px;width:440px">
  <li>Newly issued token Nov 2021 : ERC-20 token on the Beacon smart chain, trading on the griddle swap exchange under the ticker BRSK</li>
  <li>Brisk Heron token is tied to the Brisk Heron hedge fund, and is backed up by real assets (asset backed token)</li>
  <li>Brisk Heron fund is an algorithm driven fund focused on Techex megacaps, with YTD performance of 44%</li>
  <li>Through the use of the Brisk Heron token, individuals are able to use a proxy to buy and sell the fund instantly, without lockups or high minimum investments</li>
  <li>An investment in Brisk Heron provides an opportunity to invest in stocks and crypto at the same time</li>
  <li>Total coin supply is limited at 10bn, with an initial price of 0.01 USD</li>
  <li>There is full transparency regarding principles of the coin and fund</li>
</ul>

<section class="abs band about"></section>
<h2 class="abs heading sec-title" style="left:122px;top:1492px;width:480px">About the Investment Manager</h2>
<p class="abs body-text" style="left:122px;top:1588px;width:430px">Stefan Larrow is an experienced investment manager, having spent the over 20 years at leading investment firms in Europe, the Middle East and Asia, at such firms as Northgate Bank, Alpine Credit, Veritum, among others.<br>The manager has extensive experience in algorithmic investing and trading, and has proven that this methodology is far superior to traditional asset management.<br>Mr. Larrow has a Bachelor of Commerce from Hollis University in Canada, and an MBA from Ardent University in Canada.</p>
<div class="photo" style="left:615px;top:1436px;width:465px;height:387px;background:linear-gradient(100deg,#3a2318 0%,#5a3626 45%,#2a1a14 100%)" role="img" aria-label="Portrait of the investment manager in a dark suit against a wood wall"></div>

<section class="abs band coin"></section>
<div class="photo" style="left:128px;top:2001px;width:466px;height:473px;background:linear-gradient(120deg,#d9d6d2 0%,#a9a39e 30%,#1c2a4a 60%,#0e1a33 100%)" role="img" aria-label="Trader pointing at stock charts on a desktop monitor"></div>
<h2 class="abs heading sec-title" style="left:645px;top:2036px">Brisk Heron Coin</h2>
<p class="abs body-text" style="left:647px;top:2095px;width:430px">Brisk Heron LLC (“BH Fund”) is a Nevis registered hedge fund with custody services at Harbor Trust Bank. Current assets under management currently stand at USD 1.3m. The fund is an algorithm driven investment vehicle which invests in megacap technology stocks from the Techex 100 index. Current holdings include Voltra, Lumenic, Quantix, among others. The fund was started in 2021 and currently has a YTD performance of 44%, as of November 11th, 2021.</p>
<p class="abs body-text" style="left:647px;top:2280px;width:430px">We are doing an initial coin offering of 10,000,000,000 coins at an initial price of 0.01 per coin, with the intention of raising 100m USD for direct investment in the fund. Supply is capped at 10bn coins and will never increase. Supply will also be tightly controlled to limit volatility.</p>
<div class="btn" style="left:642px;top:2405px;width:172px;height:47px">Learn More</div>

<section class="abs band testi"></section>
<h2 class="abs heading sec-title" style="left:0;top:2670px;width:1200px;text-align:center">Testimonials</h2>
<div class="abs quote-badge">“</div>
<p class="abs quote">Sed ut perspiciatis unde omnis iste natus error sit voluptatem accusantium doloremque laudantium, totam rem aperiam, eaque ipsa quae ab illo inventore veritatis et quasi architecto beatae vitae dicta sunt explicabo. Nemo enim ipsam voluptatem quia voluptas sit aspernatur aut odit aut fugit, sed quia consequuntur magni dolores eos qui ratione voluptatem sequi nesciunt.</p>
<div class="abs avatar" role="img" aria-label="Customer avatar photo"></div>
<div class="abs author"><b>John Smith</b><span>Microvale</span></div>
<svg class="abs" style="left:110px;top:2834px" width="46" height="24" viewBox="0 0 46 24"><path d="M44 12H3M13 2 2 12l11 10" fill="none" stroke="#fff" stroke-width="2.5"/></svg>
<svg class="abs" style="left:1046px;top:2834px" width="46" height="24" viewBox="0 0 46 24"><path d="M2 12h41M33 2l11 10-11 10" fill="none" stroke="#fff" stroke-width="2.5"/></svg>
<div class="abs dots" style="left:572px;top:3014px"><i class="dot"></i><i class="dot on"></i><i class="dot"></i></div>

<section class="abs band blog"></section>
<h2 class="abs heading sec-title" style="left:0;top:3170px;width:1200px;text-align:center">Latest Blog</h2>
<article class="card" style="left:114px">
  <div class="card-img" style="background:linear-gradient(135deg,#1d3f7a 0%,#2b5aa8 45%,#0e1d3d 100%)" role="img" aria-label="Laptop showing trading charts"></div>
  <div class="card-body">
    <div class="card-title">Lorem ipsum dolor sit amet, consectetur adipiscing</div>
    <p class="card-text">Sed ut perspiciatis unde omnis iste natus error sit voluptatem accusantium dolorque laudantium, totam rem aperiam, eaque ipsa quae</p>
    <span class="card-more">Read more »</span>
  </div>
</article>
<article class="card" style="left:444px">
  <div class="card-img" style="background:radial-gradient(circle at 55% 45%,#d08a3a 0%,#6a3a1c 30%,#1a1c26 70%)" role="img" aria-label="Finger touching a crypto coin on a keyboard"></div>
  <div class="card-body">
    <div class="card-title">Lorem ipsum dolor sit amet, consectetur adipiscing</div>
    <p class="card-text">Sed ut perspiciatis unde omnis iste natus error sit voluptatem accusantium dolorque laudantium, totam rem aperiam, eaque ipsa quae</p>
    <span class="card-more">Read more »</span>
  </div>
</article>
<article class="card" style="left:775px">
  <div class="card-img" style="background:radial-gradient(circle at 55% 55%,#e2a55a 0%,#8a5a2a 35%,#3a2a1e 75%)" role="img" aria-label="Businessman holding glowing crypto coins"></div>
  <div class="card-body">
    <div class="card-title">Lorem ipsum dolor sit amet, consectetur adipiscing</div>
    <p class="card-text">Sed ut perspiciatis unde omnis iste natus error sit voluptatem accusantium dolorque laudantium, totam rem aperiam, eaque ipsa quae</p>
    <span class="card-more">Read more »</span>
  </div>
</article>

<footer class="abs band footer"></footer>
<div class="f-col" style="left:112px"><h4>Follow US</h4><p>Chirpline</p><p>Viewcast</p><p>Clipstream</p><p>Webpage</p><p>Threadhub</p></div>
<div class="f-col" style="left:292px"><h4>Company</h4><p>Brisk Heron</p><p>Statistics</p><p>How To Buy</p><p>Community</p></div>
<div class="f-col" style="left:492px"><h4>Contact us</h4><p>123 Your Adress Goes Here.</p><p>CA, 1234567</p><p>888 888 8888</p><p>info@briskheron.com</p></div>
<div class="f-col" style="left:776px"><h4>Subscribe to our Newsletter</h4></div>
<div class="abs email">Email Address</div>
<div class="btn" style="left:775px;top:3916px;width:313px;height:49px">Subscribe</div>
<div class="abs rule"></div>
<p class="abs copy">© 2021 Brisk Heron. All Rights Reserved.</p>

</body>
</html>
```